Real Estate Managemene Company Needs Business Card Design

We have a logo design and just need business cards made now for our business. Please use PDF logo # 3.

Card with Information to be attached shortly.

The card is used for a real estate management company. We will need to add four other employees and their cards.

Industry/Entity Type

Real Estate

Contact Information for Business Card

Tariq Hamdan
President
3187 Thornwick Avenue
Suite C
Glendale Heights, IL 60152
Phone 630.417.2286
Fax 630.417.2287
Cell 630.473.8062
vantorp@mailbreeze.net

Once design is approved we will have four other employees
Omar Hamdan
Operations Manager

Nadia Hamdan
Administrative Manager

Faz Hamdan
Principal

We would need to take out the cell # 630.473.8062 out for the remaining three cards.

Requirements
Must have
• Please use logo attached

```html
<!DOCTYPE html>
<html lang="en">
<head>
<meta charset="utf-8">
<title>Northgate Property Management Group – Business Card</title>
<link rel="stylesheet" href="https://fonts.googleapis.com/css2?family=Cinzel:wght@600&family=Marcellus&display=swap">
<style>
  :root {
    --backdrop: #a8a6a7;
    --brand-blue: #2e5a8c;
    --ink: #2b2b2b;
    --swoosh: #2a2a2a;
    --paper: #f2f2f2;
    --white: #ffffff;
    --muted: #4a4a4a;
  }
  * { margin: 0; padding: 0; box-sizing: border-box; }
  html, body { width: 1200px; height: 1200px; overflow: hidden; }
  body {
    position: relative;
    background: var(--backdrop);
    font-family: "Marcellus", Georgia, serif;
  }
  .card { position: absolute; overflow: hidden; }

  /* Front */
  .card-front {
    left: 238px; top: 117px; width: 545px; height: 420px;
    background: var(--brand-blue);
  }
  .brand-name {
    position: absolute; left: 0; right: 0; text-align: center;
    font-family: "Marcellus", Georgia, serif; font-weight: 400;
  }
  .card-front .brand-name { top: 238px; color: var(--white); }
  .brand-title { display: block; font-size: 47px; letter-spacing: 1px; line-height: 1.05; }
  .brand-sub { display: block; font-size: 17.5px; letter-spacing: 0.5px; margin-top: 2px; }

  /* Back */
  .card-back {
    left: 231px; top: 643px; width: 712px; height: 418px;
    background: var(--paper);
  }
  .wave { position: absolute; left: 0; top: 0; }
  .holder { position: absolute; right: 50px; top: 40px; text-align: right; }
  .holder-name {
    font-family: "Cinzel", Georgia, serif; font-weight: 600;
    font-size: 25px; color: var(--white); letter-spacing: 0.5px;
  }
  .holder-role { font-size: 16px; color: var(--white); margin-top: 4px; }

  .card-back .brand-name {
    left: 42px; right: auto; width: 330px; top: 220px; color: var(--ink);
  }
  .card-back .brand-title { font-size: 31px; }
  .card-back .brand-sub { font-size: 12px; margin-top: 1px; }

  .address {
    position: absolute; left: 37px; top: 334px;
    font-size: 16.5px; line-height: 24px; color: var(--muted);
  }
  .contacts {
    position: absolute; right: 48px; top: 292px;
    list-style: none; font-size: 16.5px; line-height: 23.3px; color: var(--muted);
  }
  .contacts li { display: flex; justify-content: flex-end; align-items: center; gap: 10px; }
  .contacts svg { width: 16px; height: 16px; fill: var(--brand-blue); }
</style>
</head>
<body>

  <section class="card card-front" aria-label="Card front">
    <h1 class="brand-name">
      <span class="brand-title">NORTHGATE</span>
      <span class="brand-sub">PROPERTY MANAGEMENT GROUP</span>
    </h1>
  </section>

  <section class="card card-back" aria-label="Card back">
    <svg class="wave" width="712" height="418" viewBox="0 0 712 418" aria-hidden="true">
      <path d="M0 0 H712 V168 C640 160 580 140 520 110 C440 70 360 42 250 38 C150 35 60 40 0 50 Z" fill="var(--brand-blue)"/>
      <path d="M0 62 C90 42 190 34 280 44 C380 56 450 90 530 128 C600 160 660 170 712 172 V186 C650 184 590 172 520 140 C440 104 380 72 290 58 C200 46 100 50 0 70 Z" fill="var(--swoosh)"/>
    </svg>

    <div class="holder">
      <p class="holder-name">TARIQ HAMDAN</p>
      <p class="holder-role">President</p>
    </div>

    <h2 class="brand-name">
      <span class="brand-title">NORTHGATE</span>
      <span class="brand-sub">PROPERTY MANAGEMENT GROUP</span>
    </h2>

    <address class="address" style="font-style:normal">
      3187 Thornwick Avenue<br>
      Suite C Glendale Heights, IL 60152
    </address>

    <ul class="contacts">
      <li>630.473.8062
        <svg viewBox="0 0 16 16" aria-label="Cell"><path d="M4 0h8a1 1 0 0 1 1 1v14a1 1 0 0 1-1 1H4a1 1 0 0 1-1-1V1a1 1 0 0 1 1-1zm1 2v10h6V2zm3 11a1 1 0 1 0 0 2 1 1 0 0 0 0-2z"/></svg>
      </li>
      <li>630.417.2286
        <svg viewBox="0 0 16 16" aria-label="Phone"><path d="M2 5c0-2 2-3 6-3s6 1 6 3v1h-3V4.5C10 4 9 4 8 4s-2 0-3 .5V6H2zM4 7h8l2 7H2zm4 2a2 2 0 1 0 0 4 2 2 0 0 0 0-4z"/></svg>
      </li>
      <li>630.417.2287
        <svg viewBox="0 0 16 16" aria-label="Fax"><path d="M4 1h8v4H4zM1 6h14v6h-3v3H4v-3H1zm4 5v3h6v-3z"/></svg>
      </li>
      <li>vantorp@mailbreeze.net
        <svg viewBox="0 0 16 16" aria-label="Email"><path d="M1 3h14v10H1zm1.5 1.2L8 8.5l5.5-4.3z"/></svg>
      </li>
    </ul>
  </section>

</body>
</html>
```